Company Profile for Consulting Comany

Need Company profile to be designed in a professional way.

for inspiring :-
https://www.folivane.net/gallery/5372904/COMPANY-PROFILE
https://www.folivane.net/gallery/60391742/Biotech-Product-Catalog-No1-(Laminar-Air-Flow)
https://www.folivane.net/gallery/73905218/MPG-Globalpath-Company-Profile-2014-(MPG-Rebrand-part-2)

Target Market(s)

Corporate

Industry/Entity Type

It Company

Font styles to use
Sans Serif

Requirements
Must have
• Landscape A4 size
• Must go with the logo branding
• Must Have Visual Identity is the most important
• Must Have mpty spaces

```html
<!DOCTYPE html>
<html lang="en">
<head>
<meta charset="utf-8">
<title>Northvane Advisory – Company Profile Covers</title>
<link rel="stylesheet" href="https://fonts.googleapis.com/css2?family=Montserrat:wght@400;600;700&family=Open+Sans:wght@300;400&family=Roboto+Condensed:wght@700&family=Roboto:wght@400;700&display=swap">
<style>
  :root {
    --backdrop: #bdbdbd;
    --paper: #ececec;
    --navy-deep: #141a2b;
    --navy: #24304a;
    --slate: #45536f;
    --cyan: #2aa7d6;
    --cyan-light: #5cc9ec;
    --silver-light: #f2f2f2;
    --silver-dark: #8c8c8c;
    --ink: #2a2a2a;
    --white: #ffffff;
  }
  * { box-sizing: border-box; margin: 0; padding: 0; }
  html, body { width: 969px; height: 1200px; overflow: hidden; }
  body { background: var(--backdrop); font-family: "Open Sans", sans-serif; position: relative; }

  .cover {
    position: absolute;
    left: 84px;
    width: 800px;
    height: 566px;
    background: var(--paper);
    overflow: hidden;
    box-shadow: 0 6px 18px rgba(0,0,0,0.18);
  }
  .cover--front { top: 24px; }
  .cover--back { top: 610px; }
  .cover__art { position: absolute; inset: 0; width: 100%; height: 100%; }

  .brand { position: absolute; display: flex; align-items: center; gap: 10px; }
  .brand__square { width: 30px; height: 30px; background: var(--cyan); flex: none; }
  .brand__name {
    font-family: "Montserrat", sans-serif;
    font-weight: 700;
    color: var(--cyan);
    font-size: 26px;
    line-height: 1.02;
  }
  .cover--front .brand { left: 74px; top: 70px; }
  .cover--back .brand { right: 40px; bottom: 112px; }
  .cover--back .brand__name { font-size: 22px; }

  .headline { position: absolute; left: 92px; top: 316px; color: var(--white); }
  .headline__lead { font-weight: 300; font-size: 27px; letter-spacing: 0.5px; }
  .headline__main {
    font-family: "Roboto Condensed", sans-serif;
    font-weight: 700;
    font-size: 44px;
    line-height: 1.05;
    letter-spacing: 0.5px;
  }

  .doc-label { position: absolute; right: 70px; top: 424px; text-align: right; }
  .doc-label__title { font-family: "Montserrat", sans-serif; font-size: 17px; color: var(--ink); letter-spacing: 0.5px; }
  .doc-label__url { font-family: "Montserrat", sans-serif; font-size: 11px; color: var(--cyan); margin-top: 2px; }

  .contact { position: absolute; left: 0; top: 0; width: 100%; color: var(--white); font-family: "Roboto", sans-serif; }
  .contact__title {
    position: absolute; left: 360px; top: 132px;
    font-family: "Montserrat", sans-serif; font-weight: 700;
    font-size: 18px; color: var(--cyan); letter-spacing: 0.5px;
    padding-bottom: 3px; border-bottom: 2px solid var(--cyan);
  }
  .office { position: absolute; font-size: 11px; line-height: 1.45; }
  .office--dubai { left: 215px; top: 185px; }
  .office--khobar { left: 470px; top: 228px; }
  .office__city { font-weight: 700; color: var(--cyan); font-size: 10px; letter-spacing: 0.5px; margin-bottom: 3px; }
  .office__line { display: flex; gap: 6px; align-items: flex-start; }
  .office__icon { width: 9px; height: 9px; flex: none; margin-top: 3px; fill: var(--cyan); }

  .pillars {
    position: absolute; right: 70px; bottom: 30px;
    font-family: "Montserrat", sans-serif; font-weight: 600;
    font-size: 14px; color: var(--cyan); letter-spacing: 0.5px;
    word-spacing: 6px;
  }
</style>
</head>
<body>

<section class="cover cover--front" aria-label="Front cover">
  <svg class="cover__art" viewBox="0 0 800 566">
    <defs>
      <linearGradient id="front-photo" x1="0" y1="0" x2="0.6" y2="1">
        <stop offset="0" stop-color="#1c2336"/>
        <stop offset="0.5" stop-color="#3d4a66"/>
        <stop offset="1" stop-color="#2a3550"/>
      </linearGradient>
      <linearGradient id="front-band" x1="0" y1="0" x2="1" y2="0">
        <stop offset="0" stop-color="#10141f"/>
        <stop offset="1" stop-color="#1f2a41"/>
      </linearGradient>
      <linearGradient id="front-swoosh" x1="0" y1="0" x2="1" y2="1">
        <stop offset="0" stop-color="var(--silver-light)"/>
        <stop offset="1" stop-color="var(--silver-dark)"/>
      </linearGradient>
    </defs>
    <path role="img" aria-label="Photograph: skyscrapers seen from below against a dusky sky"
          fill="url(#front-photo)"
          d="M0 0 H800 V110 L772 118 Q700 210 650 400 L0 470 Z"/>
    <path class="tagline-band" fill="url(#front-band)" opacity="0.92"
          d="M0 312 L585 300 L650 400 L0 470 Z"/>
    <polygon fill="var(--cyan-light)" points="585,300 672,306 645,352"/>
    <path fill="url(#front-swoosh)"
          d="M772 108 Q712 210 650 400 Q694 226 800 96 Z"/>
  </svg>

  <div class="brand">
    <span class="brand__square"></span>
    <span class="brand__name">Northvane<br>Advisory</span>
  </div>

  <h1 class="headline">
    <span class="headline__lead">WE CAN HELP YOU TO</span><br>
    <span class="headline__main">MAKE CHANGE HAPPEN</span>
  </h1>

  <div class="doc-label">
    <div class="doc-label__title">COMPANY PROFILE</div>
    <div class="doc-label__url">www.northvane-advisory.com</div>
  </div>
</section>

<section class="cover cover--back" aria-label="Back cover">
  <svg class="cover__art" viewBox="0 0 800 566">
    <defs>
      <linearGradient id="back-photo" x1="0" y1="0" x2="1" y2="1">
        <stop offset="0" stop-color="#2b3856"/>
        <stop offset="0.55" stop-color="#1d2740"/>
        <stop offset="1" stop-color="#3a4866"/>
      </linearGradient>
      <linearGradient id="back-swoosh" x1="1" y1="0" x2="0" y2="1">
        <stop offset="0" stop-color="var(--silver-light)"/>
        <stop offset="1" stop-color="var(--silver-dark)"/>
      </linearGradient>
    </defs>
    <path role="img" aria-label="Photograph: glass office towers rising into a cloudy blue sky"
          fill="url(#back-photo)"
          d="M0 0 H800 V500 L150 392 Q118 250 52 156 L0 150 Z"/>
    <polygon class="logo-band" fill="var(--navy-deep)" opacity="0.8" points="570,398 800,410 800,500 570,462"/>
    <polygon fill="var(--cyan-light)" points="92,332 178,348 150,392"/>
    <path fill="url(#back-swoosh)"
          d="M46 150 Q110 240 150 392 Q128 250 64 150 Z"/>
  </svg>

  <div class="contact">
    <h2 class="contact__title">CONTACT US</h2>

    <div class="office office--dubai">
      <div class="office__city">DUBAI</div>
      <div class="office__line"><svg class="office__icon" viewBox="0 0 10 10"><path d="M5 0a3.5 3.5 0 0 0-3.5 3.5C1.5 6 5 10 5 10s3.5-4 3.5-6.5A3.5 3.5 0 0 0 5 0zm0 5a1.5 1.5 0 1 1 0-3 1.5 1.5 0 0 1 0 3z"/></svg><span>PO BOX 508817, Dubai, UAE<br>14th Floor, Harbourline Court- Block B,<br>Palmera Avenue</span></div>
      <div class="office__line"><svg class="office__icon" viewBox="0 0 10 10"><path d="M2 0h2l1 2.5-1.3 1A6 6 0 0 0 6.5 6.3l1-1.3L10 6v2a2 2 0 0 1-2 2A8 8 0 0 1 0 2a2 2 0 0 1 2-2z"/></svg><span>00971 4 512 3380</span></div>
      <div class="office__line"><svg class="office__icon" viewBox="0 0 10 10"><rect x="1" y="1" width="8" height="8" rx="1"/></svg><span>00971 4 512 3391</span></div>
      <div class="office__line"><svg class="office__icon" viewBox="0 0 10 10"><path d="M0 2h10v6H0z M0 2l5 3.5L10 2"/></svg><span>info@northvane-advisory.com</span></div>
    </div>

    <div class="office office--khobar">
      <div class="office__city">KHOBAR</div>
      <div class="office__line"><svg class="office__icon" viewBox="0 0 10 10"><path d="M5 0a3.5 3.5 0 0 0-3.5 3.5C1.5 6 5 10 5 10s3.5-4 3.5-6.5A3.5 3.5 0 0 0 5 0zm0 5a1.5 1.5 0 1 1 0-3 1.5 1.5 0 0 1 0 3z"/></svg><span>PO BOX 47210, Khobar 34418,<br>SAUDI ARABIA<br>9th Floor, Corniche View Tower,<br>Al Noor St.</span></div>
      <div class="office__line"><svg class="office__icon" viewBox="0 0 10 10"><path d="M2 0h2l1 2.5-1.3 1A6 6 0 0 0 6.5 6.3l1-1.3L10 6v2a2 2 0 0 1-2 2A8 8 0 0 1 0 2a2 2 0 0 1 2-2z"/></svg><span>00966 13 871 2046</span></div>
      <div class="office__line"><svg class="office__icon" viewBox="0 0 10 10"><path d="M0 2h10v6H0z M0 2l5 3.5L10 2"/></svg><span>info@northvane-advisory.com</span></div>
    </div>
  </div>

  <div class="brand">
    <span class="brand__square"></span>
    <span class="brand__name">Northvane<br>Advisory</span>
  </div>

  <div class="pillars">STRATEGY | PEOPLE | TECHNOLOGY</div>
</section>

</body>
</html>
```